Real Estate Webpage Design

We have an existing website: brindlewoodhomes.com.au
We focus customised service mainly on Property Management and second-hand property sales.
We are not entirely happy about the current design and layout can stay roughly the same as the back end coding is linked to a CRM system.
We would like to see the design are more reachable to our clients and appearing.
Please check our Website Design Draft for more details.

Industry/Entity Type

Real estate Agency

Number of Pages Required

5+ page

Font styles to use
Sans Serif

Colors

Designer to choose colors to be used in the design.

```html
<!DOCTYPE html>
<html lang="en">
<head>
<meta charset="utf-8">
<title>Brindlewood Property Group</title>
<link href="https://fonts.googleapis.com/css2?family=Libre+Baskerville:wght@400;700&family=Poppins:wght@300;400;500;600&display=swap" rel="stylesheet">
<style>
:root{
  --gold:#d9a935;
  --navy:#1c2838;
  --ink:#222831;
  --muted:#666d77;
  --light:#f1f2f4;
  --line:#c9ccd1;
  --white:#ffffff;
}
*{box-sizing:border-box;margin:0;padding:0}
html,body{width:1200px;height:4862px;overflow:hidden}
body{font-family:"Poppins",sans-serif;color:var(--ink);background:var(--white);position:relative}
section,header,footer{position:absolute;left:0;width:1200px}
.abs{position:absolute}
.center{left:0;width:100%;text-align:center}
.eyebrow{font-family:"Libre Baskerville",serif;color:var(--gold);font-size:26px}
.title{font-family:"Libre Baskerville",serif;font-weight:700;color:var(--navy);font-size:30px;letter-spacing:.5px}
.btn{position:absolute;display:flex;align-items:center;justify-content:center;font-family:"Libre Baskerville",serif;font-weight:700;font-size:13px;letter-spacing:.5px}

/* nav */
.site-nav{top:0;height:75px;background:var(--white);box-shadow:0 1px 4px rgba(0,0,0,.08);z-index:3}
.brand{left:110px;top:14px;display:flex;align-items:center;gap:10px}
.brand-mark{width:36px;height:36px;background:var(--gold)}
.brand-name{font-size:30px;font-weight:600;color:var(--gold);line-height:1}
.nav-links{right:110px;top:28px;display:flex;gap:40px;font-size:13px;color:var(--ink)}
.nav-links .active{color:var(--gold)}

/* hero */
.hero{top:75px;height:599px;overflow:hidden}
.hero-photo{position:absolute;inset:0;background:linear-gradient(180deg,#3e4a35 0%,#5a4a3a 45%,#4a5a2e 75%,#3a4a22 100%)}
.hero-shade{position:absolute;inset:0;background:rgba(20,22,18,.45)}
.hero h1{top:175px;font-family:"Libre Baskerville",serif;font-weight:400;color:#fff;font-size:36px;line-height:52px}
.hero h1 span{color:var(--gold);font-weight:700}
.hero p{top:287px;left:300px;width:600px;text-align:center;color:#fff;font-size:13px;line-height:28px}
.hero .btn{top:393px;left:500px;width:200px;height:53px;background:var(--gold);color:var(--navy)}
.hero-wave{position:absolute;left:0;bottom:-1px}

/* welcome */
.welcome{top:674px;height:845px}
.card{position:absolute;top:237px;width:300px;height:438px;background:#fff;box-shadow:0 3px 14px rgba(0,0,0,.14);text-align:center}
.card-photo{height:240px}
.card-icon{position:absolute;left:118px;top:208px;width:64px;height:64px;border-radius:50%;background:var(--gold);display:flex;align-items:center;justify-content:center}
.card h3{margin-top:44px;font-size:15px;font-weight:500}
.card p{margin:12px 30px 0;font-size:12px;line-height:26px;color:var(--muted)}
.card .arrow{margin-top:8px}
.btn-outline-gold{top:726px;left:464px;width:272px;height:60px;border:2px solid var(--gold);color:var(--gold)}

/* properties */
.properties{top:1519px;height:840px;background:var(--light)}
.tabs{top:178px;left:310px;width:610px;height:48px;border-bottom:1px solid #d8dade;display:flex;justify-content:center;gap:60px;font-size:14px;padding-left:10px}
.tabs .active{color:var(--gold);text-align:center}
.prop{position:absolute;top:266px;width:430px}
.prop-photo{height:291px;position:relative}
.prop-photo::after{content:"";position:absolute;left:18px;top:18px;right:18px;bottom:18px;border:1px solid rgba(255,255,255,.8)}
.prop h4{margin-top:18px;font-size:16px;font-weight:600;letter-spacing:.3px}
.prop .addr{font-size:12px;color:var(--muted);margin-top:4px;display:flex;align-items:center;gap:5px}
.prop .price{font-size:19px;font-weight:600;margin-top:8px}
.prop .insp{font-size:12px;font-weight:600;margin-top:10px}
.prop .date{font-size:12px;margin-top:8px}
.prop .feats{margin-top:22px;display:flex;gap:16px;font-size:12px;align-items:center;width:400px;padding-bottom:10px;border-bottom:1px solid #dcdfe3}
.prop .feats span{display:flex;align-items:center;gap:4px}
.prop .side{position:absolute;right:12px;top:316px;display:flex;flex-direction:column;gap:10px}
.circle-arrow{position:absolute;top:392px;width:50px;height:50px;border-radius:50%;border:1px solid #b9bdc3;background:#fff;display:flex;align-items:center;justify-content:center}

/* testimonials */
.testimonials{top:2359px;height:604px}
.quote{position:absolute;top:200px;width:470px;height:266px;background:#fff;box-shadow:0 3px 14px rgba(0,0,0,.14)}
.avatar{position:absolute;left:22px;top:28px;width:86px;height:86px;border-radius:50%}
.quote-mark{position:absolute;left:30px;top:160px;font-family:"Libre Baskerville",serif;font-size:110px;color:#f0e2bd;line-height:1}
.quote p{position:absolute;left:124px;top:24px;width:320px;font-size:11.5px;font-style:italic;line-height:26px;color:var(--muted)}
.quote h5{position:absolute;left:126px;font-size:13px;font-weight:600}
.dots{top:526px;display:flex;justify-content:center;gap:6px}
.dots i{width:12px;height:12px;border-radius:50%;border:1px solid var(--navy);display:block}
.dots i.on{background:var(--navy)}

/* team */
.team{top:2963px;height:759px;background:var(--light)}
.member{position:absolute;top:181px;width:317px}
.member-photo{height:290px;background:linear-gradient(180deg,#3c3f45,#2a2c31)}
.member-info{position:absolute;top:247px;left:14px;width:289px;height:164px;background:#fff;box-shadow:0 3px 12px rgba(0,0,0,.14);text-align:center}
.member-info h4{font-family:"Libre Baskerville",serif;font-weight:700;font-size:19px;margin-top:26px;color:var(--navy)}
.member-info .role{font-size:11px;color:var(--muted);margin-top:4px}
.member-info .row{font-size:11px;margin-top:10px;display:flex;justify-content:center;align-items:center;gap:5px;color:var(--ink)}
.btn-outline-navy{top:639px;left:464px;width:272px;height:58px;border:2px solid var(--navy);color:var(--navy)}

/* contact */
.contact{top:3722px;height:669px;overflow:hidden}
.contact-photo{position:absolute;left:0;right:0;bottom:0;height:380px;background:linear-gradient(180deg,rgba(255,255,255,1) 0%,rgba(214,220,226,.6) 40%,rgba(190,198,206,.7) 100%)}
.contact .title{font-size:40px;letter-spacing:1px}
.contact .lead{top:165px;left:280px;width:640px;text-align:center;font-size:13px;line-height:26px;color:var(--muted)}
.field{position:absolute;width:350px;border-bottom:1px solid #555b63;font-size:14px;color:var(--muted);padding-bottom:14px}
.btn-submit{top:561px;left:477px;width:246px;height:56px;border-radius:28px;background:var(--navy);color:var(--gold)}

/* footer */
.site-footer{top:4391px;height:471px;background:var(--navy);color:#fff}
.footer-col{position:absolute;top:52px}
.footer-col h4{font-family:"Libre Baskerville",serif;font-weight:700;font-size:19px;letter-spacing:.3px}
.footer-col h4::after{content:"";display:block;width:40px;height:2px;background:#fff;margin-top:10px}
.footer-col ul{list-style:none;margin-top:14px;font-size:13px;line-height:30px}
.footer-col .lbl{font-size:13px;font-weight:600;margin-top:14px}
.footer-col .txt{font-size:13px;line-height:23px;display:flex;gap:6px;align-items:flex-start}
.subscribe{margin-top:20px;width:278px;height:40px;border-radius:20px;background:#fff;color:var(--ink);font-size:12px;display:flex;align-items:center;justify-content:space-between;padding:0 8px 0 20px}
.subscribe i{width:22px;height:22px;border-radius:50%;background:var(--gold);display:block}
.social{margin:22px 0 0 224px;width:48px;height:48px;border-radius:50%;border:2px solid #fff}
.footer-rule{position:absolute;left:110px;right:110px;top:402px;height:1px;background:rgba(255,255,255,.4)}
.copyright{top:426px;font-size:13px}
</style>
</head>
<body>

<header class="site-nav">
  <div class="abs brand"><div class="brand-mark"></div><div class="brand-name">Brindlewood</div></div>
  <nav class="abs nav-links"><span class="active">Home</span><span>About Us</span><span>Leasing</span><span>Buy</span><span>Sell</span><span>Our Team</span><span>Blog</span><span>Contact Us</span></nav>
</header>

<section class="hero">
  <div class="hero-photo" role="img" aria-label="Brick family home with lawn and tall trees"></div>
  <div class="hero-shade"></div>
  <h1 class="abs center">BRINDLEWOOD – A PLACE WE<br><span>“CALL HOME”</span></h1>
  <p class="abs">Brindlewood means a warm home for every family, buying a property is one of the most expensive expenses and important assets for people. Brindlewood is a real estate company located in Gungahlin, Canberra.</p>
  <div class="btn">GET STARTED</div>
  <svg class="hero-wave" width="1200" height="60" viewBox="0 0 1200 60"><path d="M0 60 L0 30 L470 30 C540 30 555 2 600 2 C645 2 660 30 730 30 L1200 30 L1200 60 Z" fill="#fff"/><path d="M600 10 V34 M592 26 L600 34 L608 26" stroke="#222" stroke-width="2" fill="none"/></svg>
</section>

<section class="welcome">
  <div class="abs center eyebrow" style="top:72px">Welcome to</div>
  <div class="abs center title" style="top:118px">BRINDLEWOOD PROPERTY GROUP</div>
  <div class="abs center" style="top:166px;font-size:13px">Your local real estate property group</div>

  <div class="card" style="left:120px">
    <div class="card-photo" role="img" aria-label="Modern single storey home with glass walls" style="background:linear-gradient(180deg,#9fc2e4,#e8e8e4 55%,#4a5a3a)"></div>
    <div class="card-icon"><svg width="32" height="32" viewBox="0 0 32 32" fill="none" stroke="#fff" stroke-width="2"><path d="M4 15 L16 5 L28 15 M8 12 V27 H24 V12 M13 27 V19 H19 V27"/></svg></div>
    <h3>Who is Brindlewood?</h3>
    <p>Brindlewood stands for a warm home, buying a property is one of the most expensive expenses</p>
    <svg class="arrow" width="30" height="14" viewBox="0 0 30 14"><path d="M2 7 H27 M21 2 L27 7 L21 12" stroke="#222" stroke-width="2" fill="none"/></svg>
  </div>
  <div class="card" style="left:450px">
    <div class="card-photo" role="img" aria-label="Hands passing a small model house" style="background:linear-gradient(180deg,#2b2b2e,#6b6460 60%,#3a3432)"></div>
    <div class="card-icon"><svg width="32" height="32" viewBox="0 0 32 32" fill="none" stroke="#fff" stroke-width="2"><path d="M5 16 L16 6 L27 16 M9 13 V26 H23 V13"/><circle cx="16" cy="19" r="3"/></svg></div>
    <h3>What do we do?</h3>
    <p>Helping landlords and vendor alike to complete efficient transactions is our signature talent.</p>
    <svg class="arrow" width="30" height="14" viewBox="0 0 30 14"><path d="M2 7 H27 M21 2 L27 7 L21 12" stroke="#222" stroke-width="2" fill="none"/></svg>
  </div>
  <div class="card" style="left:780px">
    <div class="card-photo" role="img" aria-label="Agent meeting with a happy couple at a table" style="background:linear-gradient(180deg,#d9d2c6,#8a7a68 60%,#4a4038)"></div>
    <div class="card-icon"><svg width="32" height="32" viewBox="0 0 32 32" fill="none" stroke="#fff" stroke-width="2"><path d="M4 18 L10 12 L16 16 L22 12 L28 18 L20 26 L12 26 Z M16 6 L20 10 M16 6 L12 10"/></svg></div>
    <h3>Our Promise</h3>
    <p>Brindlewood Property Group aims to at all times maintain the utmost levels of service for our customers</p>
    <svg class="arrow" width="30" height="14" viewBox="0 0 30 14"><path d="M2 7 H27 M21 2 L27 7 L21 12" stroke="#222" stroke-width="2" fill="none"/></svg>
  </div>

  <div class="btn btn-outline-gold">VIEW MORE ABOUT</div>
</section>

<section class="properties">
  <div class="abs center eyebrow" style="top:66px">Our Properties</div>
  <div class="abs center title" style="top:106px">MONTH AT BRINDLEWOOD PROPERTY GROUP</div>
  <div class="abs tabs"><span class="active">For Sale<br><svg width="14" height="14"><rect x="1" y="1" width="12" height="12" fill="none" stroke="#d9a935" stroke-width="1.5"/></svg></span><span>For Lease</span><span>Open Times</span><span>Sold</span><span>Leased</span></div>

  <div class="circle-arrow" style="left:54px"><svg width="22" height="12"><path d="M21 6 H2 M7 1 L2 6 L7 11" stroke="#222" stroke-width="1.8" fill="none"/></svg></div>
  <div class="circle-arrow" style="left:1098px"><svg width="22" height="12"><path d="M1 6 H20 M15 1 L20 6 L15 11" stroke="#222" stroke-width="1.8" fill="none"/></svg></div>

  <div class="prop" style="left:155px">
    <div class="prop-photo" role="img" aria-label="Apartment tower with a rooftop infinity pool" style="background:linear-gradient(180deg,#6e7478,#5e6c78 50%,#2e4a70)"></div>
    <h4>GUNGAHLIN</h4>
    <div class="addr"><svg width="9" height="12"><path d="M4.5 0 C2 0 0 2 0 4.5 C0 8 4.5 12 4.5 12 S9 8 9 4.5 C9 2 7 0 4.5 0Z" fill="#d9a935"/></svg>Level 3/22 Marrow Lane Gungahlin</div>
    <div class="price">$500,000+</div>
    <div class="insp">Next Inspection:</div>
    <div class="date">Sat 21st May 09:40 AM - 10:00 AM</div>
    <div class="feats"><span><svg width="16" height="10"><path d="M1 9 V1 M1 6 H15 V9 M4 4 H8" stroke="#222" stroke-width="1.6" fill="none"/></svg>2</span><span><svg width="14" height="10"><path d="M1 5 H13 C13 8 11 9 7 9 C3 9 1 8 1 5Z M3 5 V1" stroke="#222" stroke-width="1.4" fill="none"/></svg>2</span><span><svg width="16" height="10"><rect x="1" y="3" width="14" height="5" rx="1" fill="#222"/></svg>1</span></div>
    <div class="side"><svg width="12" height="12"><circle cx="6" cy="6" r="5" stroke="#444" fill="none"/></svg><svg width="12" height="12"><path d="M6 0V12M0 6H12" stroke="#444" stroke-width="2"/></svg><svg width="12" height="12"><rect x="1" y="2" width="10" height="8" stroke="#444" fill="none"/></svg><svg width="12" height="12"><path d="M6 1 L7.5 4.5 L11 5 L8.5 7.5 L9 11 L6 9 L3 11 L3.5 7.5 L1 5 L4.5 4.5Z" stroke="#444" fill="none"/></svg></div>
  </div>

  <div class="prop" style="left:617px">
    <div class="prop-photo" role="img" aria-label="Modern apartment building beside trees" style="background:linear-gradient(135deg,#3a6aa8,#7fa0c8 45%,#c9c9c6 60%,#2d3a2a)"></div>
    <h4>BELCONNEN</h4>
    <div class="addr"><svg width="9" height="12"><path d="M4.5 0 C2 0 0 2 0 4.5 C0 8 4.5 12 4.5 12 S9 8 9 4.5 C9 2 7 0 4.5 0Z" fill="#d9a935"/></svg>41/9 Fenwick Road Belconnen</div>
    <div class="price">$369,900+</div>
    <div class="insp">Next Inspection:</div>
    <div class="date">Sat 21st May 09:40 AM - 10:00 AM</div>
    <div class="feats"><span><svg width="16" height="10"><path d="M1 9 V1 M1 6 H15 V9 M4 4 H8" stroke="#222" stroke-width="1.6" fill="none"/></svg>2</span><span><svg width="14" height="10"><path d="M1 5 H13 C13 8 11 9 7 9 C3 9 1 8 1 5Z M3 5 V1" stroke="#222" stroke-width="1.4" fill="none"/></svg>2</span><span><svg width="16" height="10"><rect x="1" y="3" width="14" height="5" rx="1" fill="#222"/></svg>1</span></div>
    <div class="side"><svg width="12" height="12"><circle cx="6" cy="6" r="5" stroke="#444" fill="none"/></svg><svg width="12" height="12"><path d="M6 0V12M0 6H12" stroke="#444" stroke-width="2"/></svg><svg width="12" height="12"><rect x="1" y="2" width="10" height="8" stroke="#444" fill="none"/></svg><svg width="12" height="12"><path d="M6 1 L7.5 4.5 L11 5 L8.5 7.5 L9 11 L6 9 L3 11 L3.5 7.5 L1 5 L4.5 4.5Z" stroke="#444" fill="none"/></svg></div>
  </div>
</section>

<section class="testimonials">
  <div class="abs center eyebrow" style="top:74px">Testimonials</div>
  <div class="abs center title" style="top:120px">WHAT OUR CUSTOMERS SAYS</div>

  <div class="quote" style="left:117px">
    <div class="avatar" role="img" aria-label="Customer portrait" style="background:linear-gradient(135deg,#6d8aa0,#3d5566)"></div>
    <div class="quote-mark">“</div>
    <p>I would highly recommend Brindlewood property to you, they were helping me manage my investment property, they found a quality tenant in 2 days and maintain my property in a really good condition, they will update everything with me all the time and settle my worries. Lena, who is my PM, she is very patient and professional.</p>
    <h5 style="top:216px">TOM REID</h5>
  </div>
  <div class="quote" style="left:615px">
    <div class="avatar" role="img" aria-label="Customer portrait" style="background:linear-gradient(135deg,#e6e2dc,#b49a84)"></div>
    <div class="quote-mark">“</div>
    <p>Lena is my best property manager! Always happy to response my queries and keep us well informed at all stage. I will definitely recommend her to my friends.</p>
    <h5 style="top:216px">IVY LOWE</h5>
  </div>

  <div class="abs center dots"><i class="on"></i><i></i><i></i><i></i><i></i></div>
</section>

<section class="team">
  <div class="abs center eyebrow" style="top:70px">Team</div>
  <div class="abs center title" style="top:114px">MEET THE TEAM</div>

  <div class="member" style="left:111px">
    <div class="member-photo" role="img" aria-label="Portrait of the principal in a suit"></div>
    <div class="member-info">
      <h4>WEI TAN</h4><div class="role">Principal</div>
      <div class="row"><svg width="8" height="11"><rect x="1" y="1" width="6" height="9" rx="1" stroke="#222" fill="none"/></svg>+61 2 6000 4127 &nbsp;|&nbsp; <svg width="11" height="11"><path d="M2 1 L4 1 L5 4 L3.5 5 C4 7 5 8 7 8.5 L8 7 L10 8 L10 10 C5 10 1 6 1 2Z" fill="#222"/></svg>0400 118 352</div>
      <div class="row"><svg width="12" height="9"><rect x="0.5" y="0.5" width="11" height="8" fill="#222"/><path d="M1 1 L6 5 L11 1" stroke="#fff" fill="none"/></svg>wtan@brindlewoodhomes.com.au</div>
    </div>
  </div>
  <div class="member" style="left:442px">
    <div class="member-photo" role="img" aria-label="Portrait of the business relationship manager"></div>
    <div class="member-info">
      <h4>MIRA CHEN</h4><div class="role">Business Relationship Manager</div>
      <div class="row"><svg width="8" height="11"><rect x="1" y="1" width="6" height="9" rx="1" stroke="#222" fill="none"/></svg>+61 2 6000 4127 &nbsp;|&nbsp; <svg width="11" height="11"><path d="M2 1 L4 1 L5 4 L3.5 5 C4 7 5 8 7 8.5 L8 7 L10 8 L10 10 C5 10 1 6 1 2Z" fill="#222"/></svg>0400 226 714</div>
      <div class="row"><svg width="12" height="9"><rect x="0.5" y="0.5" width="11" height="8" fill="#222"/><path d="M1 1 L6 5 L11 1" stroke="#fff" fill="none"/></svg>mira.chen@brindlewoodhomes.com.au</div>
    </div>
  </div>
  <div class="member" style="left:772px">
    <div class="member-photo" role="img" aria-label="Portrait of the property manager"></div>
    <div class="member-info">
      <h4>LENA PARK</h4><div class="role">Property Manager</div>
      <div class="row"><svg width="8" height="11"><rect x="1" y="1" width="6" height="9" rx="1" stroke="#222" fill="none"/></svg>+61 2 6000 4127 &nbsp;|&nbsp; <svg width="11" height="11"><path d="M2 1 L4 1 L5 4 L3.5 5 C4 7 5 8 7 8.5 L8 7 L10 8 L10 10 C5 10 1 6 1 2Z" fill="#222"/></svg>0400 391 508</div>
      <div class="row"><svg width="12" height="9"><rect x="0.5" y="0.5" width="11" height="8" fill="#222"/><path d="M1 1 L6 5 L11 1" stroke="#fff" fill="none"/></svg>inspect@brindlewoodhomes.com.au</div>
    </div>
  </div>

  <div class="btn btn-outline-navy">VIEW MORE TEAM</div>
</section>

<section class="contact">
  <div class="contact-photo" role="img" aria-label="Faded row of suburban weatherboard houses"></div>
  <div class="abs center eyebrow" style="top:68px;font-size:24px">Get in Touch</div>
  <div class="abs center title" style="top:102px">CONTACT US</div>
  <p class="abs lead">Lorem ipsum dolor sit amet, consectetur adipiscing elit, sed do eiusmod tempor incididunt ut labore et dolore magna aliqua. Ut enim ad</p>
  <div class="field" style="left:227px;top:255px">First Name</div>
  <div class="field" style="left:623px;top:255px">Last Name</div>
  <div class="field" style="left:227px;top:326px">Email Address</div>
  <div class="field" style="left:623px;top:326px">Phone Number</div>
  <div class="field" style="left:227px;top:394px;width:746px;height:94px">Message</div>
  <div class="btn btn-submit">SUBMIT NOW</div>
</section>

<footer class="site-footer">
  <div class="footer-col" style="left:110px">
    <h4>QUICK LINKS</h4>
    <ul><li>Home</li><li>About Us</li><li>Leasing</li><li>Buy</li><li>Sell</li><li>Our Team</li><li>Blog</li><li>Contact Us</li></ul>
  </div>
  <div class="footer-col" style="left:302px">
    <h4>LEASING</h4>
    <ul><li>Properties for Lease</li><li>Commercial for Lease</li><li>Tenant Form</li><li>Leased Property</li><li>Lease Appraisal</li></ul>
  </div>
  <div class="footer-col" style="left:506px;width:290px">
    <h4>CONTACT US</h4>
    <div class="lbl">ADDRESS</div>
    <div class="txt"><span>Brindlewood Property Group<br>18/4 Harlow Street, Gungahlin<br>ACT 2912</span></div>
    <div class="lbl">PHONE</div>
    <div class="txt">+61 2 6000 4127</div>
    <div class="lbl">Hours</div>
    <div class="txt"><span>Monday – Friday 8:30 am – 5:00pm<br>Weekend – Closed Public holiday – Closed<br>After hour by appointment</span></div>
  </div>
  <div class="footer-col" style="left:811px;width:290px">
    <h4>NEWSLETTER</h4>
    <div class="txt" style="margin-top:14px">Lorem ipsum dolor sit amet, consectetur adipiscing elit, sed do eiusmod tempor</div>
    <div class="subscribe">Enter Email <i></i></div>
    <div class="social"></div>
  </div>
  <div class="footer-rule"></div>
  <div class="abs center copyright">© 2022. All Rights Reserved</div>
</footer>

</body>
</html>
```